New Business Card Design Project

Hi,

I'd like to create a logo for my business www.tellwickandtide.com. You will need to download two fonts for the business card: Lobster & Noticia Text. The fonts are free to download. No logo required.

Potential design idea:
One side hot pink (white font), one side white (grey font)
- On one side, hot pink similar to the pink on the website.
- Show tellwick + tide plus "your always-open wardrobe" in white font
- We really need it to be sleek, minimalistic and bright
- On the other side, we need to show our instagram and facebook URLs (pagefold.com/tellwickandtide, snapreel.com/tellwickandtide). Please use the same dark grey font as our website and use a hollowed out grey FB & Instagram logo
We also need to show the following details, website, space for name and email (hello@tellwickandtide.com).

Feel free to go as creative as you would like! The above is a safe template that we know will satisfy our needs. Aim is to minimalist, simple and bold. , Details for my new Business Card Design Project will be added soon.

• Needs to fit the prell.com luxe business card template.

```html
<!DOCTYPE html>
<html lang="en">
<head>
<meta charset="utf-8">
<title>tellwick + tide — business card</title>
<link rel="stylesheet" href="https://fonts.googleapis.com/css2?family=Noticia+Text:wght@400;700&display=swap">
<style>
  :root {
    --paper: #ffffff;
    --ink-dark: #333333;
    --ink-text: #3a3a3a;
    --rule: #8a8a8a;
    --icon: #2b2b2b;
    --trim: #ececec;
  }
  html, body {
    margin: 0;
    padding: 0;
    overflow: hidden;
    background: var(--paper);
  }
  .card {
    position: relative;
    width: 1200px;
    height: 786px;
    background: var(--paper);
    overflow: hidden;
  }
  .brand {
    position: absolute;
    right: 666px;
    top: 292px;
    text-align: right;
  }
  .brand-name {
    margin: 0;
    font-family: "Noticia Text", Georgia, serif;
    font-weight: 700;
    font-size: 62px;
    line-height: 1;
    color: var(--ink-dark);
    white-space: nowrap;
    letter-spacing: 0.5px;
  }
  .brand-tagline {
    margin: 12px 6px 0 0;
    font-family: "Noticia Text", Georgia, serif;
    font-weight: 400;
    font-size: 22px;
    line-height: 1;
    color: var(--ink-dark);
    white-space: nowrap;
  }
  .divider {
    position: absolute;
    left: 594px;
    top: 223px;
    width: 2px;
    height: 333px;
    background: var(--rule);
  }
  .contacts {
    position: absolute;
    left: 624px;
    top: 0;
    margin: 0;
    padding: 0;
    list-style: none;
  }
  .contact {
    position: absolute;
    left: 0;
    display: flex;
    align-items: center;
    white-space: nowrap;
  }
  .contact-icon {
    width: 32px;
    height: 32px;
    flex: none;
  }
  .contact-text {
    margin-left: 39px;
    font-family: "Noticia Text", Georgia, serif;
    font-size: 30px;
    color: var(--ink-text);
    line-height: 1;
  }
  .contact--social-a { top: 283px; }
  .contact--social-b { top: 345px; }
  .contact--web { top: 416px; }
  .contact--email { top: 479px; }
  .trim-mark {
    position: absolute;
    width: 1px;
    background: var(--trim);
  }
  .trim-mark--left { left: 376px; top: 662px; height: 46px; }
  .trim-mark--right { left: 768px; top: 638px; height: 44px; }
</style>
</head>
<body>
<main class="card">
  <header class="brand">
    <h1 class="brand-name">tellwick + tide</h1>
    <p class="brand-tagline">your always-open wardrobe</p>
  </header>

  <div class="divider"></div>

  <ul class="contacts">
    <li class="contact contact--social-a">
      <svg class="contact-icon" viewBox="0 0 32 32" aria-hidden="true">
        <rect x="10" y="8" width="14" height="14" fill="none" stroke="var(--icon)" stroke-width="3"/>
      </svg>
      <span class="contact-text">pagefold.com/tellwickandtide</span>
    </li>
    <li class="contact contact--social-b">
      <svg class="contact-icon" viewBox="0 0 32 32" aria-hidden="true">
        <circle cx="17" cy="16" r="8" fill="none" stroke="var(--icon)" stroke-width="3"/>
      </svg>
      <span class="contact-text">snapreel.com/tellwickandtide</span>
    </li>
    <li class="contact contact--web">
      <svg class="contact-icon" viewBox="0 0 32 32" aria-hidden="true">
        <circle cx="9" cy="23" r="3" fill="var(--icon)"/>
        <path d="M7 13 A12 12 0 0 1 19 25" fill="none" stroke="var(--icon)" stroke-width="3.2"/>
        <path d="M7 6 A19 19 0 0 1 26 25" fill="none" stroke="var(--icon)" stroke-width="3.2"/>
      </svg>
      <span class="contact-text">www.tellwickandtide.com</span>
    </li>
    <li class="contact contact--email">
      <svg class="contact-icon" viewBox="0 0 32 32" aria-hidden="true">
        <rect x="3" y="8" width="26" height="17" fill="var(--icon)"/>
        <path d="M3 8 L16 18 L29 8" fill="none" stroke="var(--paper)" stroke-width="1.6"/>
        <path d="M3 25 L12 15 M29 25 L20 15" fill="none" stroke="var(--paper)" stroke-width="1.2"/>
      </svg>
      <span class="contact-text">hello@tellwickandtide.com</span>
    </li>
  </ul>

  <div class="trim-mark trim-mark--left"></div>
  <div class="trim-mark trim-mark--right"></div>
</main>
</body>
</html>
```